Award-winnning Estate Agent needs a premium version of their 'For Sale' board design

We need a premium option for our 'For Sale' board design. We have a standard board that is attached to this brief, but were are looking to have a premium design version that we will use when selling exclusive properties. Our company name is Harbour Lane Estates and the name for this is exclusive selection is: 'The Harbour Collection'. The design needs to work with our current brand, but have a distinctive PREMIUM feel to it. I have uploaded the barnd guidelines and also some of the exisisting logo variations. We do NOT need a new logo but feel free to play around with colours, fonts, sizes etc. for the sign.

Target Market(s)

Property buyers & house hunters

Industry/Entity Type

Real Estate - Residential Property

Font styles to use
Sans Serif

Requirements
Must have
• A premium fee, must be square design, must be easy to read when driving past the sign
Nice to have
• I'm open ot ideas

```html
<!DOCTYPE html>
<html lang="en">
<head>
<meta charset="utf-8">
<title>Harbour Lane Estates – For Sale Board</title>
<link rel="stylesheet" href="https://fonts.googleapis.com/css2?family=Archivo:wdth,wght@100,500;100,700;125,900&display=swap">
<style>
  :root {
    --navy: #283891;
    --sky: #29a8e0;
    --white: #ffffff;
    --page: #ffffff;
  }
  * { margin: 0; padding: 0; box-sizing: border-box; }
  html, body {
    width: 909px;
    height: 1200px;
    overflow: hidden;
    background: var(--page);
    font-family: "Archivo", "Helvetica Neue", Arial, sans-serif;
  }
  .canvas {
    position: relative;
    width: 909px;
    height: 1200px;
  }
  .board {
    position: absolute;
    left: 24px;
    top: 170px;
    width: 860px;
    height: 860px;
    background: var(--white);
    box-shadow: 0 2px 10px rgba(0, 0, 0, 0.12);
  }
  .board-panel {
    position: absolute;
    left: 52px;
    top: 53px;
    width: 756px;
    height: 754px;
    background: var(--navy);
    color: var(--white);
  }
  .headline,
  .phone {
    position: absolute;
    left: 38px;
    width: 680px;
    overflow: visible;
  }
  .headline { top: 24px; height: 92px; }
  .phone { top: 564px; height: 88px; }
  .headline text {
    font-family: "Archivo", "Arial Black", sans-serif;
    font-stretch: 125%;
    font-weight: 900;
    font-size: 116px;
  }
  .phone text {
    font-family: "Archivo", Arial, sans-serif;
    font-weight: 700;
    font-size: 112px;
  }
  .shadow { fill: var(--sky); }
  .face { fill: var(--white); }
  .rule {
    position: absolute;
    left: 38px;
    width: 678px;
    height: 2px;
    background: var(--sky);
  }
  .rule--top { top: 136px; }
  .rule--mid { top: 544px; }
  .rule--low { top: 667px; }
  .brand {
    position: absolute;
    left: 0;
    top: 196px;
    width: 100%;
    display: flex;
    flex-direction: column;
    align-items: center;
    gap: 42px;
  }
  .brand-mark {
    width: 96px;
    height: 96px;
    background: var(--white);
  }
  .brand-name {
    font-weight: 500;
    font-size: 56px;
    line-height: 1;
    letter-spacing: -0.5px;
    color: var(--white);
  }
  .collection-band {
    position: absolute;
    left: 38px;
    top: 446px;
    width: 678px;
    height: 78px;
    background: var(--sky);
    display: flex;
    align-items: center;
    justify-content: center;
  }
  .collection-name {
    font-weight: 700;
    font-size: 54px;
    line-height: 1;
    color: var(--white);
  }
  .web-address {
    position: absolute;
    left: 0;
    top: 684px;
    width: 100%;
    text-align: center;
    font-weight: 700;
    font-size: 42px;
    line-height: 1;
    color: var(--white);
  }
</style>
</head>
<body>
<main class="canvas">
  <section class="board" aria-label="Harbour Lane Estates For Sale board">
    <div class="board-panel">
      <svg class="headline" viewBox="0 0 680 92" aria-label="For Sale">
        <text class="shadow" x="4" y="90" textLength="676" lengthAdjust="spacingAndGlyphs">FOR SALE</text>
        <text class="face" x="0" y="86" textLength="676" lengthAdjust="spacingAndGlyphs">FOR SALE</text>
      </svg>
      <div class="rule rule--top"></div>

      <div class="brand">
        <div class="brand-mark"></div>
        <p class="brand-name">Harbour Lane Estates</p>
      </div>

      <div class="collection-band">
        <p class="collection-name">The Harbour Collection</p>
      </div>
      <div class="rule rule--mid"></div>

      <svg class="phone" viewBox="0 0 680 88" aria-label="01632 960418">
        <text class="shadow" x="3" y="86" textLength="676" lengthAdjust="spacingAndGlyphs">01632 960418</text>
        <text class="face" x="0" y="83" textLength="676" lengthAdjust="spacingAndGlyphs">01632 960418</text>
      </svg>
      <div class="rule rule--low"></div>

      <p class="web-address">www.harbourlaneestates.co.uk</p>
    </div>
  </section>
</main>
</body>
</html>
```